Book Cover for Harbor Wishes Holiday Voyage Needed!

Gable Meadow Publications needs a cover for a novella. We will need an ebook cover and print wrap. We need to stay with the brand we have as indicated by the files attached. Take a look for the brand and style we are looking for.
Here are the specifics:
Title (subject to change): Harbor Wishes
Subtitle: A Christmas Novella
Series Name: The Lantern Cove Love Series (Book 3.5)
Author: Mirela Dunford

Target Market(s)

Romance readers

Industry/Entity Type

Entertainment Industry

Font styles to use
Other font styles liked:
• NovitoNova - Title, Neumann - Subtitle

Colors
3276b5
33a6d7
33b8a4
abd036
fbee3d
ffc214

Requirements
Must have
• Please take a look at the other three covers to stay on brand and for inspiration
Nice to have
• Possibly something with a criuse ship.
Should not have
• Not looking for "real" images or depictions. We want a scene with bright colors same as the previous books but with a bit of a casual feel.

```html
<!DOCTYPE html>
<html lang="en">
<head>
<meta charset="utf-8">
<title>Harbor Wishes – A Christmas Novella</title>
<link rel="stylesheet" href="https://fonts.googleapis.com/css2?family=Big+Shoulders+Display:wght@200&family=Handlee&family=Cinzel:wght@500&family=Alegreya+SC&display=swap">
<style>
  :root {
    --page: #ffffff;
    --sky-deep: #1d6cbf;
    --sky: #3a93d6;
    --cloud: #dfeef6;
    --sea-deep: #1e9fc9;
    --sea: #46c6dc;
    --shallows: #a9e6e6;
    --sand: #f3e6e2;
    --palm: #3d6b2e;
    --ribbon: #3f8fd0;
    --ribbon-edge: #c9463d;
    --title-fill: #ffffff;
    --title-line: #30485e;
    --ink: #2f3a44;
    --author: #1f262c;
  }
  * { box-sizing: border-box; margin: 0; padding: 0; }
  html, body {
    width: 1200px; height: 1200px; overflow: hidden;
    background: var(--page);
  }
  .cover {
    position: absolute;
    left: 362px; top: 219px;
    width: 477px; height: 760px;
    overflow: hidden;
  }
  .cover-scene {
    position: absolute; inset: 0;
    background:
      radial-gradient(ellipse 38% 30% at 95% 12%, rgba(61,107,46,0.85), rgba(61,107,46,0) 70%),
      radial-gradient(ellipse 40% 30% at 5% 100%, var(--sand), rgba(243,230,226,0) 70%),
      linear-gradient(180deg,
        var(--sky-deep) 0%,
        var(--sky) 28%,
        var(--cloud) 48%,
        var(--sky) 58%,
        var(--sea-deep) 66%,
        var(--sea) 80%,
        var(--shallows) 100%);
  }
  .series-ribbon {
    position: absolute;
    left: 38px; top: 56px;
    width: 386px; height: 40px;
  }
  .series-ribbon svg { position: absolute; inset: 0; }
  .series-name {
    position: absolute; inset: 0;
    display: flex; align-items: center; justify-content: center;
    font-family: "Alegreya SC", serif;
    font-size: 15.5px;
    color: #ffffff;
    letter-spacing: 0.2px;
    white-space: nowrap;
  }
  .title {
    position: absolute;
    left: 0; right: 0;
    text-align: center;
    font-family: "Big Shoulders Display", sans-serif;
    font-weight: 200;
    color: var(--title-fill);
    -webkit-text-stroke: 1.2px var(--title-line);
    text-shadow: 0 2px 6px rgba(20,40,60,0.35);
    line-height: 1;
  }
  .title-top { top: 146px; font-size: 122px; letter-spacing: 1px; }
  .title-main { top: 258px; font-size: 232px; letter-spacing: 2px; }
  .subtitle {
    position: absolute;
    left: 0; right: 0; top: 520px;
    text-align: center;
    font-family: "Handlee", cursive;
    font-size: 35px;
    color: var(--ink);
  }
  .author {
    position: absolute;
    left: 0; right: 0; top: 632px;
    text-align: center;
    font-family: "Cinzel", serif;
    font-weight: 500;
    font-size: 32px;
    letter-spacing: 4px;
    color: var(--author);
  }
</style>
</head>
<body>
  <main class="cover">
    <div class="cover-scene" role="img" aria-label="Bright tropical beach scene: blue sky with white clouds, a palm frond at the top right, turquoise shallow water and a pale sandy shoreline with a small boat"></div>

    <div class="series-ribbon">
      <svg width="386" height="40" viewBox="0 0 386 40" aria-hidden="true">
        <path d="M4 6 Q193 0 382 4 L378 34 Q193 30 8 38 Z" fill="var(--ribbon-edge)"/>
        <path d="M6 8 Q193 2 380 6 L376 32 Q193 28 10 36 Z" fill="var(--ribbon)"/>
      </svg>
      <span class="series-name">The Lantern Cove Love Series (Book 3.5)</span>
    </div>

    <h1>
      <span class="title title-top">HARBOR</span>
      <span class="title title-main">WISHES</span>
    </h1>
    <p class="subtitle">A Christmas Novella...</p>
    <p class="author">MIRELA DUNFORD</p>
  </main>
</body>
</html>
```